Coming Soon page for a new fitness startup

We are a new startup based in Toronto, Canada working on a site and mobile app where people can register for athletic events such as running, cycling, triathlon, SUP, etc.

Participants will also be able to manage their clubs and team, and connect their fitness trackers so they have all their fitness data and friends in one place.

I like very simple designs and lots of whitespace. So no need for icons or unnecessary graphics.

I prefer having a mobile phone app instead of a hero image. No need to worry about the details within the mobile app for now, we can fill it in later. Here are some landing pages that I like.
https://pixelvault.example/torvanmelk/buckets/438197-Landing-Page

Attached is a wireframe that gives some sample content for each of the sections. Please do not take the wireframe too literally, it is only meant to illustrate the content that we are experimenting with and should give an idea of how much text will be on the page.

I have also attached the company logo files. The logo is not being used yet so feel free to simplify the logo if it doesn't look great with your design. For example, I'm ok with just the name "k7ravi" in white if that looks better.

Target Market(s)

Ages 25 to 45. Interested in running, cycling, triathlon, SUP, etc.

Industry/Entity Type

Fitness

Coding

Coded - Design and coding required

Number of Pages Required

1 page

Requirements
Should not have
• Any photos should not contain track and field events, or people in a gym. Any photos should have people running or cycling outdoors. I know that photos can be easily swapped out but it is distracting to review a design that has the wrong photos.

```html
<!DOCTYPE html>
<html lang="en">
<head>
<meta charset="utf-8">
<title>k7ravi — Coming Soon</title>
<link rel="stylesheet" href="https://fonts.googleapis.com/css2?family=Exo+2:wght@600;700;800&family=Jost:wght@400;500;600&display=swap">
<style>
:root{
  --red:#d42030;
  --red-dark:#b81a28;
  --ink:#2b2b2b;
  --text:#4a4a4a;
  --muted:#8a8a8a;
  --line:#bdbdbd;
  --topbar:#58595b;
  --soft:#f5f5f5;
  --white:#ffffff;
}
*{box-sizing:border-box;margin:0;padding:0}
html,body{width:1200px;height:2187px;overflow:hidden}
body{position:relative;background:var(--white);font-family:"Jost",sans-serif;color:var(--text)}
.abs{position:absolute}

/* top bar */
.topbar{left:0;top:0;width:1200px;height:41px;background:var(--topbar)}
.social-dot{width:26px;height:26px;border-radius:50%;border:2px solid var(--white);top:8px}
.phone-icon{left:930px;top:8px;width:26px;height:26px;border-radius:50%;background:var(--white)}
.phone-num{left:966px;top:10px;color:var(--white);font-size:15px;font-weight:500;letter-spacing:.3px;line-height:20px}

/* header */
.brand{display:flex;align-items:center;gap:10px}
.brand-mark{border-radius:50%;background:var(--red)}
.brand-name{font-family:"Jost",sans-serif;font-weight:500;color:var(--ink)}
.header-brand{left:141px;top:54px}
.header-brand .brand-mark{width:54px;height:54px}
.header-brand .brand-name{font-size:46px;line-height:1}
.launch-pill{left:806px;top:52px;width:251px;height:38px;border-radius:19px;background:var(--red);color:var(--white);font-weight:600;font-size:17px;display:flex;align-items:center;padding-left:52px}
.pill-dot{position:absolute;left:4px;top:4px;width:30px;height:30px;border-radius:50%;background:var(--white)}

/* hero */
.hero{left:0;top:122px;width:1200px;height:493px;background:linear-gradient(180deg,#8f9a8a 0%,#c9b07a 35%,#e3a24a 55%,#7a5a36 78%,#3b3025 100%)}
.hero-panel{left:140px;top:201px;width:583px;height:336px;background:rgba(70,60,50,.72);padding:28px 27px}
.hero-title{font-family:"Exo 2",sans-serif;font-weight:800;color:var(--white);font-size:29px;line-height:39px;text-transform:uppercase;letter-spacing:.8px;white-space:nowrap}
.hero-lede{color:var(--white);font-size:14.5px;line-height:21px;margin-top:8px;width:500px}
.hero-invite{color:var(--white);font-size:20.5px;line-height:29px;margin-top:14px;width:495px}
.notify{display:flex;margin-top:17px;height:40px;width:432px}
.notify-input{flex:1;background:var(--white);border-radius:20px 0 0 20px;font-size:15px;color:var(--ink);padding:10px 22px}
.notify-btn{width:108px;background:var(--red);color:var(--white);font-size:15px;border-radius:0 20px 20px 0;display:flex;align-items:center;justify-content:center}
.hero-badge{left:676px;top:322px;width:100px;height:100px;border-radius:50%;background:var(--white);border:4px solid var(--red)}
.slide-arrow{top:334px;width:70px;height:70px;border-radius:50%;background:var(--red)}
.slide-arrow svg{position:absolute;top:23px}

/* phone */
.device{left:803px;top:200px;width:225px;height:456px;border-radius:34px;background:#f4f4f2;border:2px solid #d6d0c4;box-shadow:0 14px 28px rgba(0,0,0,.18)}
.device-speaker{left:100px;top:22px;width:24px;height:3px;border-radius:2px;background:#333}
.device-cam{left:79px;top:21px;width:6px;height:6px;border-radius:50%;background:#333}
.device-screen{left:9px;top:47px;width:203px;height:360px;background:var(--white);border:1px solid #ccc}
.device-home{left:97px;top:414px;width:28px;height:28px;border-radius:50%;border:2px solid #bbb}
.screen-brand{left:28px;top:88px}
.screen-brand .brand-mark{width:36px;height:36px}
.screen-brand .brand-name{font-size:34px}
.screen-field{left:18px;width:173px;height:28px;border:1px solid #d3d3d3;font-size:11px;color:#555;padding:6px 6px}
.screen-login{left:61px;top:254px;width:88px;height:27px;border-radius:14px;background:var(--red);color:var(--white);font-size:14px;text-align:center;line-height:27px}

/* section heading */
.section-title{width:1200px;left:0;text-align:center;font-family:"Exo 2",sans-serif;font-weight:700;font-size:29px;color:var(--ink);letter-spacing:.4px;text-transform:uppercase}
.section-title em{font-style:normal;color:var(--red)}
.divider{height:1px;background:var(--line)}
.divider-dot{width:24px;height:24px;border-radius:50%;border:2px solid var(--red);background:var(--white)}

.tagline{left:0;width:1200px;top:812px;text-align:center;color:var(--red);font-size:19px;text-transform:uppercase}

/* feature cards */
.feature{top:869px;width:251px;height:122px;border:1px solid #9a9a9a;padding:9px 6px 0 72px}
.feature.is-active{border-color:var(--red)}
.feature-title{font-size:12px;font-weight:600;text-transform:uppercase;color:#555;margin-bottom:3px;white-space:nowrap;line-height:17px}
.feature.is-active .feature-title{color:var(--red)}
.feature-body{font-size:12.5px;line-height:20.5px;color:#555;white-space:nowrap}
.feature-icon{width:88px;height:88px;border-radius:50%;background:var(--white);border:3px solid #555;top:885px}
.feature-icon.is-active{border-color:var(--red)}
.feature-icon svg{position:absolute;left:22px;top:22px}

/* organizer */
.organizer{left:0;top:1064px;width:1200px;height:446px;background:var(--soft)}
.calendar-art{left:208px;top:1134px;width:300px;height:314px;border-radius:4px;background:linear-gradient(180deg,#e85a5a 0 18%,#eeeeee 18% 100%)}
.org-title{left:628px;top:1134px;font-family:"Exo 2",sans-serif;font-weight:700;font-size:27px;color:var(--ink);text-transform:uppercase}
.org-title em{font-style:normal;color:var(--red)}
.org-sub{left:628px;top:1226px;color:var(--red);font-size:19px;font-weight:400}
.org-body{left:628px;top:1268px;width:434px;font-size:14.5px;line-height:25px;letter-spacing:.8px;color:#444}
.pill-btn{height:36px;border-radius:18px;background:var(--red);color:var(--white);font-size:17px;display:flex;align-items:center;padding-left:50px}
.org-btn{left:628px;top:1401px;width:272px}

/* contact */
.field{border:1px solid #b5b5b5;border-radius:3px;font-size:11px;color:#555;padding:9px 10px;background:var(--white)}
.send-btn{left:528px;top:1822px;width:144px;padding-left:60px}

/* footer */
.footer{left:0;top:1932px;width:1200px;height:214px;background:linear-gradient(180deg,#3a3d4c 0%,#2a2c38 55%,#4a3f3a 100%)}
.footer-badge{left:547px;top:1897px;width:104px;height:104px;border-radius:50%;background:var(--white);border:4px solid #555}
.footer-social{top:2030px;width:34px;height:34px;border-radius:50%;background:var(--white)}
.footer-links{left:0;width:1200px;top:2093px;text-align:center;color:var(--white);font-size:17px;word-spacing:2px}
.footer-links span{margin:0 14px}
.copyright{left:0;top:2146px;width:1200px;height:41px;background:var(--red);color:var(--white);font-size:13px;text-align:center;line-height:41px}
</style>
</head>
<body>

<!-- top bar -->
<div class="abs topbar"></div>
<div class="abs social-dot" style="left:809px" aria-label="Social link"></div>
<div class="abs social-dot" style="left:849px" aria-label="Social link"></div>
<div class="abs social-dot" style="left:889px" aria-label="Social link"></div>
<div class="abs phone-icon">
  <svg width="26" height="26" viewBox="0 0 26 26"><path d="M9 7c1 0 1.5 2.5 2 3.5.3.7-1 1.5-1 2 .5 1.5 2 3 3.5 3.5.5 0 1.3-1.3 2-1 1 .5 3.5 1 3.5 2s-1.5 2-2.5 2C12 19 7 14 7 9c0-1 1-2 2-2z" fill="#58595b"/></svg>
</div>
<div class="abs phone-num">555 014 2290</div>

<!-- header -->
<div class="abs brand header-brand"><span class="brand-mark"></span><span class="brand-name">k7ravi</span></div>
<div class="abs launch-pill"><span class="pill-dot"></span>Launching Spring 2018</div>

<!-- hero -->
<div class="abs hero" role="img" aria-label="Photo of a cyclist riding on an open road at sunset"></div>
<div class="abs hero-panel">
  <h1 class="hero-title">Connect your training, friends,<br>and events in one place</h1>
  <p class="hero-lede">Lorem ipsum dolor sit amet, consectetur adipiscing elit. Maecenas luctus lacinia neque, blandit rutrum elit pellentesque ut. Donec elementum.</p>
  <p class="hero-invite">Join our email list. A referral program is coming and you'll want to be the first to know.</p>
  <div class="notify"><div class="notify-input">Email Address</div><div class="notify-btn">NOTIFY ME</div></div>
</div>
<div class="abs hero-badge"></div>
<div class="abs slide-arrow" style="left:-35px"><svg style="left:45px" width="14" height="24" viewBox="0 0 14 24"><path d="M11 3 3 12l8 9" stroke="#fff" stroke-width="3.5" fill="none"/></svg></div>
<div class="abs slide-arrow" style="left:1165px"><svg style="left:12px" width="14" height="24" viewBox="0 0 14 24"><path d="m3 3 8 9-8 9" stroke="#fff" stroke-width="3.5" fill="none"/></svg></div>

<!-- phone -->
<div class="abs device">
  <div class="abs device-cam"></div>
  <div class="abs device-speaker"></div>
  <div class="abs device-screen">
    <div class="abs brand screen-brand"><span class="brand-mark"></span><span class="brand-name">k7ravi</span></div>
    <div class="abs screen-field" style="top:170px">Email</div>
    <div class="abs screen-field" style="top:208px">Password</div>
    <div class="abs screen-login">Log In</div>
  </div>
  <div class="abs device-home"></div>
</div>

<!-- training section -->
<h2 class="abs section-title" style="top:712px">Training and racing <em>all in one place</em></h2>
<div class="abs divider" style="left:290px;top:777px;width:620px"></div>
<div class="abs divider-dot" style="left:588px;top:765px"></div>
<p class="abs tagline">A new fitness community is coming soon.</p>

<div class="abs feature is-active" style="left:176px">
  <h3 class="feature-title">Find Events</h3>
  <p class="feature-body">Lorem ipsum dolor sit amet,<br>consectetur adipiscing elit.<br>Lorem ipsum dolor sit amet,<br>Maecenas luctus lacinia...[+]</p>
</div>
<div class="abs feature-icon is-active" style="left:140px">
  <svg width="44" height="44" viewBox="0 0 44 44"><rect x="4" y="8" width="30" height="28" rx="3" fill="none" stroke="#d42030" stroke-width="3"/><path d="M4 16h30M12 4v8M26 4v8" stroke="#d42030" stroke-width="3"/><circle cx="33" cy="33" r="8" fill="#fff" stroke="#d42030" stroke-width="3"/><path d="M33 29v4h3" stroke="#d42030" stroke-width="2" fill="none"/></svg>
</div>

<div class="abs feature" style="left:491px">
  <h3 class="feature-title">Invite Your Friends</h3>
  <p class="feature-body">Lorem ipsum dolor sit amet,<br>consectetur adipiscing elit.<br>Lorem ipsum dolor sit amet,<br>Maecenas luctus lacinia...[+]</p>
</div>
<div class="abs feature-icon" style="left:455px">
  <svg width="44" height="44" viewBox="0 0 44 44"><circle cx="19" cy="13" r="8" fill="#555"/><path d="M5 38c0-9 6-14 14-14s10 3 12 6v8z" fill="#555"/><circle cx="33" cy="33" r="7" fill="#fff" stroke="#555" stroke-width="2.5"/><path d="M33 29v8M29 33h8" stroke="#555" stroke-width="2.5"/></svg>
</div>

<div class="abs feature" style="left:806px">
  <h3 class="feature-title">Connect Your Workouts</h3>
  <p class="feature-body">Lorem ipsum dolor sit amet,<br>consectetur adipiscing elit.<br>Lorem ipsum dolor sit amet,<br>Maecenas luctus lacinia...[+]</p>
</div>
<div class="abs feature-icon" style="left:770px">
  <svg width="44" height="44" viewBox="0 0 44 44"><rect x="18" y="4" width="18" height="30" rx="3" fill="none" stroke="#555" stroke-width="3"/><path d="M6 40l6-16c2-3 6-3 8 0l3 5-6 11z" fill="#555"/></svg>
</div>

<!-- organizer section -->
<div class="abs organizer"></div>
<div class="abs calendar-art" role="img" aria-label="Illustration of a wall calendar with a red alarm clock"></div>
<h2 class="abs org-title">Organizing <em>an event?</em></h2>
<div class="abs divider-dot" style="left:628px;top:1180px"></div>
<div class="abs divider" style="left:676px;top:1192px;width:366px"></div>
<h3 class="abs org-sub">Attracting Participants Is Hard</h3>
<p class="abs org-body">With Your Event Listed On K7ravi We'll Not Only Handle The Rregistration And Payment Process, We've Also Made It Our Own Personal Mission To Drive Up Participation Numbers Across All Events.</p>
<div class="abs pill-btn org-btn"><span class="pill-dot"></span>Contact Us To Learn More</div>

<!-- contact -->
<h2 class="abs section-title" style="top:1576px">We'd love to <em>hear from you</em></h2>
<div class="abs divider" style="left:394px;top:1638px;width:175px"></div>
<div class="abs divider-dot" style="left:588px;top:1626px"></div>
<div class="abs divider" style="left:631px;top:1638px;width:178px"></div>
<div class="abs field" style="left:141px;top:1674px;width:452px;height:30px">Your Name</div>
<div class="abs field" style="left:606px;top:1674px;width:452px;height:30px">Email Address</div>
<div class="abs field" style="left:141px;top:1724px;width:917px;height:62px">How Can We Help?</div>
<div class="abs pill-btn send-btn"><span class="pill-dot"></span>Send</div>

<!-- footer -->
<div class="abs footer" role="img" aria-label="Photo of the Toronto skyline at dusk"></div>
<div class="abs footer-badge"></div>
<div class="abs footer-social" style="left:514px" aria-label="Social link"></div>
<div class="abs footer-social" style="left:560px" aria-label="Social link"></div>
<div class="abs footer-social" style="left:606px" aria-label="Social link"></div>
<div class="abs footer-social" style="left:652px" aria-label="Social link"></div>
<nav class="abs footer-links">About Us <span>|</span> Developers <span>|</span> Careers</nav>
<div class="abs copyright">Copyright © 2018 k7ravi Inc. &nbsp;|&nbsp; All rights reserved.</div>

</body>
</html>
```